Consulting business card

*1) An Overview:* The business is simply a financial transaction wherein I
offer to provide advice to financial holders of commercial real estate
mortgages (which are sub-performing or non-performing), and said holders
are desirous of selling said mortgages which I will offer advice to said
holders in the purchase of said mortgages. Please note the attached copy
of a proposed line-by-line business card which starts with the 1st line
"KRW Advisory, LLC" with the 2nd line "Purchase of Commercial Mortgage
Loan" and the 3rd line "Sub-performing and Non-performing" is my desired
copy subject to any suggested changes. Please ignore the the copy below
the aforementioned proposed card/copy as it will be activated at a later
date.and advise
*2) The Target Market:* I contact and advise senior officers in banks,
insurance companies, and financial institutions such as CEOs, CFOs, COOs,
and Loan Mitigation Officers: the senior officers are tasked with the
removal of sub-performing and non-performing commercial real estate loans
from their real estate portfolios. The desired market is targeted at $1-10
million USD and located in the US.
*3) Design Specifics: *STYLE should be conservative and be representative
of the financial market contacts; COLOR might show a rich forest green
element, a gold foil accent, and subtle black printing, however,
alternatively, silver foil accent(s) with strong black print would seem in
harmony with the services offered, however, I would appreciate any artful
suggestions; IMAGERY should be subtle (no logo can be strong enough to make
an immediate impact): the quality should make the recipient feel he/she has
just met an experienced and competent financial adviser (I have over 55
years of successful financial and business experience).
720.217.6154davidfredrickjones@gmail.com

```html
<!DOCTYPE html>
<html lang="en">
<head>
<meta charset="utf-8">
<title>KRW Advisory, LLC – Business Card</title>
<link href="https://fonts.googleapis.com/css2?family=Tinos:wght@400;700&family=Arimo:wght@400&display=swap" rel="stylesheet">
<style>
  :root {
    --page-bg: #e7e4df;
    --card-light: #f4f3f1;
    --card-mid: #dfe1e3;
    --forest-green: #1f7a35;
    --forest-green-dark: #16602a;
    --gold-light: #d9a445;
    --gold-deep: #a86f1f;
    --ink: #222222;
    --ink-soft: #2f2f2f;
  }
  * { margin: 0; padding: 0; box-sizing: border-box; }
  html, body { width: 1200px; height: 970px; overflow: hidden; background: var(--page-bg); }
  .card {
    position: absolute; left: 50px; top: 156px;
    width: 1100px; height: 658px;
    background: linear-gradient(160deg, var(--card-light) 0%, var(--card-mid) 100%);
    box-shadow: 0 10px 30px rgba(0,0,0,0.18);
    overflow: hidden;
  }
  .card__swoosh { position: absolute; inset: 0; width: 100%; height: 100%; }
  .tagline, .company-name, .person-name, .person-title, .contact-line {
    position: absolute; white-space: nowrap; color: var(--ink);
  }
  .tagline {
    left: 62px; font-family: "Tinos", serif; font-weight: 700;
    font-size: 43px; color: var(--ink-soft); line-height: 1;
  }
  .tagline--first { top: 56px; }
  .tagline--second { top: 124px; }
  .company-name {
    left: 60px; top: 180px; font-family: "Tinos", serif; font-weight: 700;
    font-size: 70px; line-height: 1;
  }
  .person-name {
    right: 55px; top: 350px; font-family: "Tinos", serif; font-weight: 400;
    font-size: 56px; line-height: 1; color: #111;
  }
  .person-title {
    right: 58px; top: 418px; font-family: "Arimo", sans-serif;
    font-size: 33px; line-height: 1;
  }
  .contact-line {
    right: 56px; font-family: "Arimo", sans-serif; font-size: 28px; line-height: 1;
    display: flex; align-items: center; gap: 26px;
  }
  .contact-line--phone { top: 492px; }
  .contact-line--email { top: 541px; }
  .contact-line--address { top: 594px; }
  .contact-icon { width: 23px; height: 23px; flex: none; }
</style>
</head>
<body>
  <div class="card">
    <svg class="card__swoosh" viewBox="0 0 1100 658" preserveAspectRatio="none" aria-hidden="true">
      <defs>
        <linearGradient id="goldFoil" x1="0" y1="0" x2="1" y2="1">
          <stop offset="0" stop-color="var(--gold-light)"/>
          <stop offset="0.55" stop-color="#c98a35"/>
          <stop offset="1" stop-color="var(--gold-deep)"/>
        </linearGradient>
        <linearGradient id="greenBand" x1="0" y1="1" x2="1" y2="0">
          <stop offset="0" stop-color="var(--forest-green-dark)"/>
          <stop offset="1" stop-color="var(--forest-green)"/>
        </linearGradient>
      </defs>
      <path class="gold-field" d="M0,612 C350,480 800,300 1100,335 L1100,658 L0,658 Z" fill="url(#goldFoil)"/>
      <path class="green-band" d="M0,603 C330,445 780,232 1040,254 Q1092,260 1100,288 L1100,335 C800,300 350,480 0,612 Z" fill="url(#greenBand)"/>
    </svg>

    <p class="tagline tagline--first">The Purchase of Commercial Mortgage Loans</p>
    <p class="tagline tagline--second">Sub-performing and Non-performing Loans</p>
    <h1 class="company-name">KRW Advisory, LLC</h1>

    <p class="person-name">Martin R. Halloway</p>
    <p class="person-title">Managing Member</p>

    <p class="contact-line contact-line--phone">555.384.9027
      <svg class="contact-icon" viewBox="0 0 24 24" aria-hidden="true"><rect width="24" height="24" rx="2" fill="#111"/><path d="M5 10 Q12 4 19 10 L17 12 L15 10 L9 10 L7 12 Z M7 13 H17 V18 H7 Z" fill="#fff"/></svg>
    </p>
    <p class="contact-line contact-line--email">martinhalloway@examplemail.net
      <svg class="contact-icon" viewBox="0 0 24 24" aria-hidden="true"><rect width="24" height="24" rx="2" fill="#111"/><rect x="5" y="7" width="14" height="10" fill="#fff"/><path d="M5 7 L12 13 L19 7" fill="none" stroke="#111" stroke-width="1.5"/></svg>
    </p>
    <p class="contact-line contact-line--address">0748 Alder Lane Ridgeview, CO 80000
      <svg class="contact-icon" viewBox="0 0 24 24" aria-hidden="true"><rect width="24" height="24" rx="2" fill="#111"/><path d="M12 5 A4.5 4.5 0 0 1 16.5 9.5 C16.5 13 12 18 12 18 C12 18 7.5 13 7.5 9.5 A4.5 4.5 0 0 1 12 5 Z" fill="#fff"/><circle cx="12" cy="9.5" r="1.6" fill="#111"/></svg>
    </p>
  </div>
</body>
</html>
```